TelvaLaw a fully remote and fully bilingual law firm for the Florida injured

1. Can you describe what your company does?- a solo lawyer practice in Florida, D.C., and soon in NY. I offer services for auto accidents, negligence, boat accident, motorcycle accident, insurance claims, premises liability, and things of the like.

2. Who are your target customers for the website? Drivers, passengers, pedestrians involved in accidents where they were injured and need help making a claim against the other vehicle or insurance company- throughout the entire state of Florida, but primarily in greater central florida area for english speaking and latino community offering a 100% bilingual services ENGLISH/SPANISH and 100% remote, where I wont make clients come to an office ever, and will private online meetings, signing portals, and all to have it efficient for clients benefit.

3. Do you have an existing domain name / website address? yes, telvalaw.com through google workspace. i need help in getting in brought to you so you can handle it please.

4. In addition to a Home Page, which other pages / sections would you like your website to have:
About Us
Contact Us
Products / Services
Office / Mailing Address
Testimonials / Reviews
FAQs
Terms and Conditions
Any other page / section you would like- DO EVERYTHING IN BOTH LANGUAGES- ENGLISH AND SPANISH
I want the page to have a way for people to calendar appts with me. and also
to make transactions - accepting all methods of payment

For each of the pages / sections you’d like to have, please provide the text (and images, if available) you would like to include.

5. Which of the below are features and functionalities your website will need:
Image Gallery
Videos
Contact Form
Mailing List
Maps
FAQs
Accepting payments / donations
6. Please provide the URLs for the social media profiles you'd like to link to the website. I have none, I am just starting, I actually want to have the online presence ready before my official launch.

Target Market(s)

Injured individuals by the negligent act of another in Florida

Industry/Entity Type

LAWYER/ AUTO ACCIDENT/NEGLIGENCE/ PREMISES LIABILITY/ CIVIL LAW

Coding

Coded - Design and coding required

Number of Pages Required

1 page

Requirements
Must have
• bilingual ENGLISH and SPANISH; a button for people to calendar appointments with me; accept payments, and to be able to integrate with major software like docusign, adobe, etc since I need to integrate under the fully remote platform
Nice to have
• look at my logo from markforge.com it has the Telvarique Law and TelvaLaw.com together.. I have the telvalaw.com domain from google. need you guys to help integrate that too , meaning to be able to use that domain for my website.

```html
<!DOCTYPE html>
<html lang="en">
<head>
<meta charset="utf-8">
<title>Blog – Telvarique Law</title>
<link rel="stylesheet" href="https://fonts.googleapis.com/css2?family=Poppins:ital,wght@0,300;0,400;0,500;0,600;1,400&family=Cinzel:wght@500&family=Oswald:wght@500;600&display=swap">
<style>
:root{
  --navy:#1d3264;
  --ink:#1f1f1f;
  --gold:#c9972f;
  --text:#666666;
  --line:#dcdcdc;
  --mist:#f2f2f2;
  --white:#ffffff;
  --night:#060606;
}
*{box-sizing:border-box;margin:0;padding:0}
html,body{width:1200px;height:3388px;overflow:hidden}
body{position:relative;font-family:"Poppins",sans-serif;color:var(--text);background:var(--white)}
a{color:inherit;text-decoration:none}
ul{list-style:none}

/* ---------- hero ---------- */
.hero{position:absolute;left:0;top:0;width:1200px;height:557px;background:var(--mist);overflow:hidden}
.hero-photo{position:absolute;inset:0 0 40px 0;background:linear-gradient(100deg,#1b2a4d 0%,#2c3f68 40%,#5d6f92 70%,#8f9bb3 100%)}
.hero-curve{position:absolute;left:0;top:430px;width:1200px;height:127px}
.brand{position:absolute;left:14px;top:14px;width:190px;text-align:center;color:var(--white)}
.brand-mark{width:56px;height:56px;border:2px solid var(--white);border-radius:50%;margin:0 auto 10px}
.brand-name{font-size:14px;font-weight:500;letter-spacing:3px;white-space:nowrap}
.main-nav{position:absolute;left:218px;top:33px;width:500px;display:flex;justify-content:space-between;font-size:12.8px;color:var(--white);white-space:nowrap}
.main-nav .active{color:var(--gold)}
.lang{position:absolute;left:740px;top:27px;width:83px;height:29px;border:1.5px solid var(--white);border-radius:15px;color:var(--white);font-size:12px;display:flex;align-items:center;justify-content:center;gap:6px}
.lang-flag{width:22px;height:14px;background:#2a3d7a;border:1px solid #fff}
.nav-sep{position:absolute;left:836px;top:22px;width:1px;height:38px;background:rgba(255,255,255,.35)}
.pay-btn{position:absolute;left:853px;top:22px;width:150px;height:37px;border-radius:19px;background:var(--gold);color:var(--white);font-size:13px;display:flex;align-items:center;justify-content:center}
.call{position:absolute;left:1015px;top:22px;display:flex;gap:8px;color:var(--white)}
.call-icon{width:37px;height:37px;border-radius:50%;background:var(--gold);display:flex;align-items:center;justify-content:center}
.call small{display:block;font-size:12.5px;opacity:.85;line-height:16px}
.call strong{display:block;font-size:17px;font-weight:500;line-height:22px}
.hero-copy{position:absolute;left:141px;top:164px;width:370px;color:var(--white)}
.hero-title{font-family:"Cinzel",serif;font-weight:500;font-size:40px;line-height:55px;padding-left:18px;border-left:3px solid var(--gold)}
.hero-lede{margin-top:28px;font-size:12.8px;line-height:22.5px;text-align:left}
.consult-btn{position:absolute;left:142px;top:348px;width:254px;height:42px;border-radius:21px;background:var(--gold);color:var(--white);font-size:13px;display:flex;align-items:center;justify-content:center;gap:10px}
.scroll-cue{position:absolute;left:580px;top:485px;width:38px;height:38px;border-radius:50%;background:var(--white);display:flex;align-items:center;justify-content:center;box-shadow:0 2px 6px rgba(0,0,0,.12)}
.breadcrumb{position:absolute;left:141px;top:526px;font-size:13px;color:#7189b5;display:flex;gap:10px}
.breadcrumb .current{color:var(--navy)}

/* ---------- blog heading ---------- */
.section-title{position:absolute;left:0;top:636px;width:1200px;text-align:center;font-family:"Oswald",sans-serif;font-weight:600;font-size:34px;letter-spacing:3px;color:var(--navy)}
.section-rule{position:absolute;left:575px;top:690px;width:50px;height:2px;background:var(--gold)}

/* ---------- article ---------- */
.post{position:absolute;left:141px;top:720px;width:601px;min-height:2131px;border:1px solid var(--line);padding:0 22px 24px}
.post-photo{height:297px;margin:-1px -23px 0;background:linear-gradient(120deg,#5d6065 0%,#9a9ea4 45%,#d9dde2 75%,#6c8fb3 100%)}
.post-title{margin-top:28px;font-size:19px;font-weight:500;color:var(--ink);line-height:26px}
.post-meta{margin-top:12px;font-size:13.5px;color:var(--ink)}
.post-meta .label{color:var(--gold)}
.post-meta em{font-style:italic}
.post-meta .gap{margin-left:26px}
.post-intro{margin-top:16px}
p{font-size:12.8px;line-height:22.5px;text-align:justify;margin-bottom:13px}
.post-part{border-top:1px solid var(--line);padding-top:26px;margin-top:18px}
.post-part h3{font-size:16px;font-weight:500;color:var(--ink);margin-bottom:12px}
.ticks{margin-top:-2px}
.ticks li{font-size:12.8px;color:var(--ink);line-height:22.5px;margin-bottom:7px;display:flex;align-items:center;gap:10px;padding-left:10px}
.tick{width:15px;height:15px;border-radius:50%;background:var(--gold);display:flex;align-items:center;justify-content:center;flex:none}
.share{margin-top:14px;font-size:14px;font-weight:500;color:var(--navy);display:flex;align-items:center;gap:8px}

/* ---------- sidebar ---------- */
.widget{position:absolute;left:769px;width:290px;border:1px solid var(--line)}
.search{top:720px;height:111px;padding:18px 16px}
.widget-label{font-size:17px;font-weight:500;color:var(--ink)}
.search-field{margin-top:14px;height:42px;background:var(--mist);display:flex;align-items:center;gap:12px;padding-left:12px;font-size:13px;color:#9a9a9a}
.widget-head{height:49px;background:var(--gold);color:var(--white);font-size:17px;font-weight:500;padding:0 16px;display:flex;align-items:center}
.cats{top:862px;height:233px}
.cats ul{padding:0 16px}
.cats li{height:59px;border-bottom:1px solid var(--line);display:flex;align-items:center;gap:12px;font-size:14.5px;color:var(--ink)}
.cats li:last-child{border-bottom:none}
.recent{top:1125px;height:586px}
.recent ul{padding:12px 16px 0}
.recent li{height:107px;border-bottom:1px solid var(--line);display:flex;gap:16px;padding-top:6px}
.recent li:last-child{border-bottom:none}
.thumb{width:71px;height:71px;flex:none}
.recent h4{font-size:14.5px;font-weight:500;color:var(--ink);margin-top:12px}
.recent time{display:flex;align-items:center;gap:10px;font-size:13.5px;color:var(--ink);margin-top:10px}

/* ---------- footer ---------- */
.footer{position:absolute;left:0;top:2920px;width:1200px;height:468px;color:var(--white)}
.footer-shape{position:absolute;left:0;top:0;width:1200px;height:468px}
.footer-brand{position:absolute;left:56px;top:153px;width:262px;text-align:center}
.footer-brand .brand-mark{width:82px;height:82px;margin-bottom:18px}
.footer-brand .brand-name{font-size:20px;letter-spacing:4px}
.socials{display:flex;gap:9px;justify-content:center;margin-top:28px}
.socials span{width:31px;height:31px;border-radius:50%;border:1.5px solid var(--white)}
.socials span:first-child{background:#1f3b7a;border-color:#1f3b7a}
.foot-col{position:absolute;top:152px}
.foot-col h5{font-family:"Oswald",sans-serif;font-weight:500;font-size:17px;letter-spacing:2.5px}
.foot-col h5::after{content:"";display:block;width:32px;height:2px;background:var(--gold);margin-top:10px}
.foot-col li{font-size:13px;line-height:27.6px}
.links{left:414px}
.links ul,.services ul{margin-top:12px}
.services{left:624px}
.contact{left:871px}
.contact ul{margin-top:12px}
.contact li{display:flex;gap:12px;line-height:19px;margin-bottom:16px;font-size:13px}
.contact svg{flex:none;margin-top:2px}
.foot-rule{position:absolute;left:70px;top:401px;width:1060px;height:1px;background:rgba(255,255,255,.25)}
.copyright{position:absolute;left:70px;top:424px;font-size:13px}
.copyright a{font-weight:500}
.cards{position:absolute;left:903px;top:418px;display:flex;gap:4px}
.cards span{width:41px;height:27px;border-radius:3px}
</style>
</head>
<body>

<header class="hero">
  <div class="hero-photo" role="img" aria-label="Lawyer signing a contract beside scales of justice"></div>
  <svg class="hero-curve" viewBox="0 0 1200 127" preserveAspectRatio="none" aria-hidden="true">
    <path d="M0 23 Q600 125 1200 23 L1200 127 L0 127 Z" fill="#f2f2f2"/>
    <path d="M0 20 Q600 120 1200 20" fill="none" stroke="#ffffff" stroke-width="6"/>
    <path d="M0 15 Q600 112 1200 15" fill="none" stroke="#c9972f" stroke-width="4"/>
  </svg>

  <a class="brand" href="#">
    <div class="brand-mark"></div>
    <div class="brand-name">TELVARIQUE LAW</div>
  </a>

  <nav class="main-nav">
    <a href="#">Home</a><a href="#">About Us</a><a href="#">Services</a><a href="#">Testimonials</a><a href="#">FAQ's</a><a class="active" href="#">Blog</a><a href="#">Contact Us</a>
  </nav>
  <div class="lang"><span class="lang-flag"></span>EN
    <svg width="8" height="6" viewBox="0 0 8 6"><path d="M1 1l3 3 3-3" stroke="#fff" fill="none" stroke-width="1.3"/></svg>
  </div>
  <div class="nav-sep"></div>
  <a class="pay-btn" href="#">Make a Payment</a>
  <div class="call">
    <span class="call-icon"><svg width="17" height="17" viewBox="0 0 24 24"><path fill="#fff" d="M6.6 10.8a15.1 15.1 0 0 0 6.6 6.6l2.2-2.2c.3-.3.7-.4 1-.2 1.1.4 2.3.6 3.6.6.6 0 1 .4 1 1V20c0 .6-.4 1-1 1A17 17 0 0 1 3 4c0-.6.4-1 1-1h3.5c.6 0 1 .4 1 1 0 1.3.2 2.5.6 3.6.1.3 0 .7-.2 1z"/></svg></span>
    <div><small>Call Us Today</small><strong>123 456 7890</strong></div>
  </div>

  <div class="hero-copy">
    <h1 class="hero-title">Blog</h1>
    <p class="hero-lede">Bilingual legal services for auto accidents, negligence claims, and personal injury cases throughout Florida, DC, and soon NY. 100% remote consultations available.</p>
  </div>
  <a class="consult-btn" href="#">Schedule Free Consultation
    <svg width="24" height="12" viewBox="0 0 24 12"><path d="M0 6h22M17 1l5 5-5 5" stroke="#fff" fill="none" stroke-width="1.5"/></svg>
  </a>
  <span class="scroll-cue"><svg width="18" height="10" viewBox="0 0 18 10"><path d="M1 1l8 8 8-8" stroke="#1d3264" fill="none" stroke-width="2"/></svg></span>
  <div class="breadcrumb"><a href="#">Home</a><span>»</span><a href="#">Blog</a><span>»</span><span class="current">What to Do Immediately After a Car Accident in Florida</span></div>
</header>

<h2 class="section-title">BLOG</h2>
<div class="section-rule"></div>

<article class="post">
  <div class="post-photo" role="img" aria-label="Personal accident claim form on a clipboard next to a damaged car"></div>
  <h1 class="post-title">What to Do Immediately After a Car Accident in Florida</h1>
  <div class="post-meta"><span class="label">Date:</span> 20 Nov 2025 - <em>Posted By Admin</em><span class="gap label">Categories:</span> General Articles</div>
  <div class="post-intro">
    <p>On the other hand, we denounce with righteous indignation and dislike men who are so beguiled and demoralized by the charms of pleasure of the moment, so blinded by desire, that they cannot foresee the pain and trouble that are bound to ensue; and equal blame belongs to those who fail in their duty through weakness of will, which is the same as saying through shrinking from toil and pain. These cases are perfectly simple and easy to distinguish.</p>
  </div>

  <section class="post-part">
    <h3>1. The standard Lorem Ipsum passage, used since the</h3>
    <p>But I must explain to you how all this mistaken idea of denouncing pleasure and praising pain was born and I will give you a complete account of the system, and expound the actual teachings of the great explorer of the truth, the master-builder of human happiness. No one rejects, dislikes,</p>
    <p>Nor again is there anyone who loves or pursues or desires to obtain pain of itself, because it is pain, but because occasionally circumstances occur in which toil and pain can procure him some great pleasure.</p>
  </section>

  <section class="post-part">
    <h3>2. What to Do Immediately After a Car Accident in Florida</h3>
    <p>There are many variations of passages of Lorem Ipsum available, but the majority have suffered alteration in some form, by injected humour.</p>
    <p>Randomised words which don't look even slightly believable. If you are going to use a passage of Lorem Ipsum, you need to be sure there isn't anything embarrassing hidden in the middle of text.</p>
    <p>All the Lorem Ipsum generators on the Internet tend to repeat predefined chunks as necessary, making this the first true generator on the Internet.</p>
  </section>

  <section class="post-part">
    <h3>3. Where can I get some?</h3>
    <p>Lorem ipsum dolor sit amet, consectetur adipiscing elit, sed do eiusmod tempor incididunt ut labore et dolore magna aliqua. Ut enim ad minim veniam, quis nostrud exercitation ullamco laboris nisi ut aliquip ex ea commodo consequat. Duis aute irure dolor in reprehenderit in voluptate velit esse cillum dolore eu fugiat nulla pariatur.</p>
    <p>Sed ut perspiciatis unde omnis iste natus error sit voluptatem accusantium doloremque laudantium, totam rem aperiam.</p>
  </section>

  <section class="post-part">
    <h3>4. Ut enim ad minim veniam, quis nostrud exercitation ullamco</h3>
    <p>All the Lorem Ipsum generators on the Internet tend to repeat predefined chunks as necessary, making this the first true generator on the Internet.</p>
    <ul class="ticks">
      <li><span class="tick"><svg width="9" height="7" viewBox="0 0 9 7"><path d="M1 3.5l2.3 2.3L8 1" stroke="#fff" fill="none" stroke-width="1.5"/></svg></span>On the other hand, we denounce with righteous indignation and dislike men</li>
      <li><span class="tick"><svg width="9" height="7" viewBox="0 0 9 7"><path d="M1 3.5l2.3 2.3L8 1" stroke="#fff" fill="none" stroke-width="1.5"/></svg></span>But in certain circumstances and owing to the claims of duty or the obligations</li>
      <li><span class="tick"><svg width="9" height="7" viewBox="0 0 9 7"><path d="M1 3.5l2.3 2.3L8 1" stroke="#fff" fill="none" stroke-width="1.5"/></svg></span>he rejects pleasures to secure other greater pleasures, or else</li>
      <li><span class="tick"><svg width="9" height="7" viewBox="0 0 9 7"><path d="M1 3.5l2.3 2.3L8 1" stroke="#fff" fill="none" stroke-width="1.5"/></svg></span>I will give you a complete account of the system, and expound</li>
    </ul>
  </section>

  <section class="post-part">
    <h3>5. Nemo enim ipsam voluptatem quia aut odit aut fugit</h3>
    <p>But I must explain to you how all this mistaken idea of denouncing pleasure and praising pain was born and I will give you a complete account of the system, and expound the actual teachings of the great explorer of the truth, the master-builder of human happiness. No one rejects, dislikes,</p>
    <p>Nor again is there anyone who loves or pursues or desires to obtain pain of itself, because it is pain, but because occasionally circumstances occur in which toil and pain can procure him some great pleasure.</p>
  </section>

  <section class="post-part">
    <h3>6. Conclusion</h3>
    <p>There are many variations of passages of Lorem Ipsum available, but the majority have suffered alteration in some form, by injected humour.</p>
    <p>Randomised words which don't look even slightly believable. If you are going to use a passage of Lorem Ipsum, you need to be sure there isn't anything embarrassing hidden in the middle of text.</p>
    <p>All the Lorem Ipsum generators on the Internet tend to repeat predefined chunks as necessary, making this the first true generator on the Internet.</p>
  </section>

  <a class="share" href="#">
    <svg width="16" height="16" viewBox="0 0 16 16" fill="none" stroke="#1d3264" stroke-width="1.3"><circle cx="12.5" cy="3" r="2"/><circle cx="3" cy="8" r="2"/><circle cx="12.5" cy="13" r="2"/><path d="M4.8 7l5.9-3M4.8 9l5.9 3"/></svg>
    Share It
  </a>
</article>

<aside>
  <div class="widget search">
    <div class="widget-label">Search</div>
    <div class="search-field">
      <svg width="16" height="16" viewBox="0 0 16 16" fill="none" stroke="#1d3264" stroke-width="1.5"><circle cx="6.5" cy="6.5" r="5"/><path d="M10.3 10.3L15 15"/></svg>
      Search here
    </div>
  </div>

  <div class="widget cats">
    <div class="widget-head">Categories</div>
    <ul>
      <li><svg width="18" height="14" viewBox="0 0 18 14" fill="none" stroke="#1d3264" stroke-width="2"><path d="M2 1l6 6-6 6M9 1l6 6-6 6"/></svg>General Articles</li>
      <li><svg width="18" height="14" viewBox="0 0 18 14" fill="none" stroke="#1d3264" stroke-width="2"><path d="M2 1l6 6-6 6M9 1l6 6-6 6"/></svg>Photos</li>
      <li><svg width="18" height="14" viewBox="0 0 18 14" fill="none" stroke="#1d3264" stroke-width="2"><path d="M2 1l6 6-6 6M9 1l6 6-6 6"/></svg>Videos</li>
    </ul>
  </div>

  <div class="widget recent">
    <div class="widget-head">Recent Posts</div>
    <ul>
      <li><div class="thumb" role="img" aria-label="Client reviewing documents at a desk" style="background:linear-gradient(135deg,#3d5a80,#c9c2b5)"></div>
        <div><h4>Premises Explained</h4><time><svg width="15" height="15" viewBox="0 0 16 16" fill="none" stroke="#c9972f" stroke-width="1.4"><circle cx="8" cy="8" r="6.5"/><path d="M8 4v4l2.5 1.5"/></svg>20 Nov 2025</time></div></li>
      <li><div class="thumb" role="img" aria-label="Legal advice paperwork on a desk" style="background:linear-gradient(135deg,#e8e3d8,#8a7d6b)"></div>
        <div><h4>Remote Legal Help</h4><time><svg width="15" height="15" viewBox="0 0 16 16" fill="none" stroke="#c9972f" stroke-width="1.4"><circle cx="8" cy="8" r="6.5"/><path d="M8 4v4l2.5 1.5"/></svg>20 Nov 2025</time></div></li>
      <li><div class="thumb" role="img" aria-label="Motorcycle down on a road" style="background:linear-gradient(180deg,#6f8a5a,#4a4f55)"></div>
        <div><h4>Florida Accident Laws</h4><time><svg width="15" height="15" viewBox="0 0 16 16" fill="none" stroke="#c9972f" stroke-width="1.4"><circle cx="8" cy="8" r="6.5"/><path d="M8 4v4l2.5 1.5"/></svg>20 Nov 2025</time></div></li>
      <li><div class="thumb" role="img" aria-label="Driver on a phone call after a crash" style="background:linear-gradient(135deg,#b9b2a6,#5e5a55)"></div>
        <div><h4>Car Accident Tips</h4><time><svg width="15" height="15" viewBox="0 0 16 16" fill="none" stroke="#c9972f" stroke-width="1.4"><circle cx="8" cy="8" r="6.5"/><path d="M8 4v4l2.5 1.5"/></svg>20 Nov 2025</time></div></li>
      <li><div class="thumb" role="img" aria-label="Damaged car after a collision" style="background:linear-gradient(135deg,#7c8894,#3b4148)"></div>
        <div><h4>Insurance Claim Myths</h4><time><svg width="15" height="15" viewBox="0 0 16 16" fill="none" stroke="#c9972f" stroke-width="1.4"><circle cx="8" cy="8" r="6.5"/><path d="M8 4v4l2.5 1.5"/></svg>20 Nov 2025</time></div></li>
    </ul>
  </div>
</aside>

<footer class="footer">
  <svg class="footer-shape" viewBox="0 0 1200 468" preserveAspectRatio="none" aria-hidden="true">
    <path d="M0 22 Q600 120 1200 22 L1200 468 L0 468 Z" fill="#060606"/>
    <path d="M0 18 Q600 112 1200 18" fill="none" stroke="#c9972f" stroke-width="5"/>
  </svg>

  <div class="footer-brand">
    <div class="brand-mark"></div>
    <div class="brand-name">TELVARIQUE LAW</div>
    <div class="socials" aria-label="Social profiles"><span></span><span></span><span></span><span></span></div>
  </div>

  <div class="foot-col links">
    <h5>QUICK LINKS</h5>
    <ul><li>Home</li><li>About Us</li><li>Services</li><li>Testimonials</li><li>FAQ's</li><li>Contact Us</li><li>Make a Payment</li></ul>
  </div>
  <div class="foot-col services">
    <h5>SERVICES</h5>
    <ul><li>Auto Accident</li><li>Negligence</li><li>Motorcycle Accident</li><li>Motorcycle Accident</li><li>Insurance Claims</li><li>Motorcycle Accident</li></ul>
  </div>
  <div class="foot-col contact">
    <h5>CONTACT DETAILS</h5>
    <ul>
      <li><svg width="14" height="17" viewBox="0 0 14 17"><path fill="#c9972f" d="M7 0a7 7 0 0 0-7 7c0 5 7 10 7 10s7-5 7-10a7 7 0 0 0-7-7zm0 9.5A2.5 2.5 0 1 1 7 4.5a2.5 2.5 0 0 1 0 5z"/></svg><span>123, Loream Ipsum Dollar Road,<br>Florida. FL - 123 456</span></li>
      <li><svg width="15" height="15" viewBox="0 0 24 24"><path fill="#c9972f" d="M6.6 10.8a15.1 15.1 0 0 0 6.6 6.6l2.2-2.2c.3-.3.7-.4 1-.2 1.1.4 2.3.6 3.6.6.6 0 1 .4 1 1V20c0 .6-.4 1-1 1A17 17 0 0 1 3 4c0-.6.4-1 1-1h3.5c.6 0 1 .4 1 1 0 1.3.2 2.5.6 3.6.1.3 0 .7-.2 1z"/></svg><span>(555) 123-4567</span></li>
      <li><svg width="15" height="12" viewBox="0 0 15 12"><rect width="15" height="12" rx="1.5" fill="#c9972f"/><path d="M1 1.5l6.5 5 6.5-5" stroke="#060606" fill="none" stroke-width="1.2"/></svg><span>info@telvalaw.com</span></li>
      <li><svg width="15" height="15" viewBox="0 0 16 16" fill="none" stroke="#c9972f" stroke-width="1.6"><circle cx="8" cy="8" r="6.5"/><path d="M8 4v4l2.5 1.5"/></svg><span>Monday - Friday: 9:00 AM - 6:00 PM<br>Weekends: By appointment only</span></li>
    </ul>
  </div>

  <div class="foot-rule"></div>
  <div class="copyright">© 2025 Telvarique Law. All rights reserved. &nbsp;|&nbsp; <a href="#">Terms and Conditions</a></div>
  <div class="cards" aria-label="Accepted payment methods">
    <span style="background:#2c8fd6"></span><span style="background:#4a5560"></span><span style="background:#e9e9e9"></span><span style="background:#f4f4f4"></span><span style="background:#f7f7f7"></span>
  </div>
</footer>

</body>
</html>
```